Bay & Meadow Property Services Tri-fold sales & marketing brochure

We need a tri-fold brochure that describes our three lines of business and the various services within each line to use in sales and marketing efforts.
See website for additional background info:
https://halvernq7.example-host.com/

Target Market(s)

Real Estate Investors & owners in Residential Rental, Short-term Rentals, and Mini/Maxi Storage Rental markets

Requirements
Must have
• See attached logo, use color scheme & font styles to match. Make sure to utilize photos to enhance look/feel.

```html
<!DOCTYPE html>
<html lang="en">
<head>
<meta charset="utf-8">
<title>Bay &amp; Meadow Property Services – Tri-fold Brochure</title>
<link href="https://fonts.googleapis.com/css2?family=Tinos:wght@400;700&display=swap" rel="stylesheet">
<style>
  :root{
    --brand-blue:#00a5cc;
    --brand-blue-dark:#0089ad;
    --ink:#111111;
    --ink-soft:#222222;
    --navy-text:#0d3b4c;
    --paper:#ffffff;
    --mist:#d5e9f3;
    --black-arc:#1c1c1c;
    --canvas:#ffffff;
  }
  *{box-sizing:border-box;margin:0;padding:0}
  html,body{width:1200px;height:1200px;overflow:hidden;background:var(--canvas)}
  body{position:relative;font-family:"Tinos","Times New Roman",serif;color:var(--ink)}
  .sheet{position:absolute;width:745px;height:526px;overflow:hidden;background:var(--paper)}
  .sheet--outside{left:232px;top:52px}
  .sheet--inside{left:230px;top:629px}
  .sheet-art{position:absolute;inset:0;width:745px;height:526px}
  .panel{position:absolute;top:0;width:248px;height:526px}
  .panel--1{left:0}.panel--2{left:248px}.panel--3{left:497px}

  /* Outside: about panel */
  .about{position:absolute;left:32px;top:120px;width:173px}
  .about h1{font-size:25px;color:var(--brand-blue);font-weight:700;line-height:1;margin-bottom:6px}
  .about p{font-size:7.6px;line-height:9.6px;text-align:justify;color:var(--ink-soft);margin-bottom:9px}
  .about h2{font-size:12px;color:var(--brand-blue);font-weight:700;margin:4px 0 7px}
  .reason{font-size:7.2px;line-height:9.6px;margin-bottom:9px;color:var(--ink-soft)}
  .reason b{color:var(--ink)}

  /* Outside: contact panel */
  .contact{position:absolute;left:0;width:248px;text-align:center;font-size:10px;color:var(--ink)}
  .contact--phone{top:48px}
  .contact--email{top:70px}
  .contact--address{top:470px;font-size:9.6px;line-height:12.5px;color:var(--navy-text)}

  /* Outside: cover panel */
  .brand-name{position:absolute;left:25px;top:26px;font-size:24px;font-weight:700;color:var(--ink)}
  .cover-title{position:absolute;right:31px;top:330px;text-align:right;font-size:26.5px;line-height:32px;font-weight:700}
  .cover-title .dark{color:var(--ink)}
  .cover-title .light{color:var(--paper)}
  .cover-tagline{position:absolute;left:0;width:248px;top:483px;text-align:center;font-size:9.8px;color:var(--ink)}

  /* Inside panels */
  .service{position:absolute;left:32px;width:190px}
  .service h2{font-size:16px;font-weight:700;color:var(--brand-blue);line-height:1.1}
  .service p{font-size:9px;line-height:11.6px;text-align:justify;color:var(--ink-soft)}
  .residential{top:186px}
  .residential h2{margin-bottom:12px}
  .residential h3{font-size:12.5px;line-height:15px;font-weight:700;color:var(--brand-blue);margin:6px 0 9px}
  .residential .small{font-size:7.4px;line-height:9.6px}
  .callout{font-weight:700;text-align:center;color:var(--ink)}
  .residential .callout{font-size:15.5px;line-height:19px;margin-top:6px}

  .short-term{top:316px;left:28px}
  .short-term h2{color:var(--ink);text-align:center;margin-bottom:10px}
  .short-term p{font-size:8.7px;line-height:11.6px;color:#eaf8fc}
  .short-term .callout{color:var(--paper);font-size:15.5px;line-height:19px;margin-top:14px}

  .storage{top:215px;left:24px;width:196px}
  .storage h2{margin-bottom:20px}
  .storage p{font-size:8.5px;line-height:11.6px}
  .storage .callout{font-size:19.5px;line-height:25px;margin-top:16px}
  .storage .closing{text-align:center;font-size:13.5px;line-height:18px;margin-top:18px;color:var(--ink)}
</style>
</head>
<body>

<!-- Outside of the brochure -->
<section class="sheet sheet--outside" aria-label="Brochure outside">
  <svg class="sheet-art" viewBox="0 0 745 526" aria-hidden="false">
    <defs>
      <linearGradient id="foldShade" x1="0" x2="1">
        <stop offset="0" stop-color="#e9e9e9"/><stop offset=".5" stop-color="#ffffff"/><stop offset="1" stop-color="#efefef"/>
      </linearGradient>
      <linearGradient id="aerialTones" x1="0" y1="0" x2="1" y2="1">
        <stop offset="0" stop-color="#a9b8a4"/><stop offset=".5" stop-color="#5f9a4e"/><stop offset="1" stop-color="#3d6b3a"/>
      </linearGradient>
      <linearGradient id="blueFade" x1="0" x2="1">
        <stop offset="0" stop-color="#0096bb"/><stop offset="1" stop-color="#00a9d0"/>
      </linearGradient>
      <clipPath id="coverPanel"><rect x="497" y="0" width="248" height="526"/></clipPath>
    </defs>

    <!-- middle panel shading -->
    <rect x="248" y="0" width="249" height="526" fill="url(#foldShade)"/>

    <!-- cover panel -->
    <g clip-path="url(#coverPanel)">
      <rect x="497" y="0" width="248" height="526" fill="url(#blueFade)"/>
      <g role="img" aria-label="Aerial photo of a suburban neighbourhood with trees and houses">
        <path d="M497 0 H745 V220 C690 230 640 270 600 330 L497 330 Z" fill="url(#aerialTones)"/>
      </g>
      <path d="M497 0 H745 V220 C690 230 640 270 600 330 L497 330 Z" fill="none"/>
      <path d="M497 0 H520 C520 0 497 0 497 0 Z" fill="#fff"/>
      <!-- black wedge top right -->
      <path d="M648 0 H745 V175 C725 110 690 45 648 0 Z" fill="var(--black-arc)"/>
      <path d="M640 0 C675 30 700 70 715 90" stroke="var(--brand-blue)" stroke-width="6" fill="none"/>
      <!-- blue sweep on left of cover -->
      <path d="M497 86 C560 110 600 200 600 330 C600 400 560 470 497 526 Z" fill="var(--brand-blue)" opacity=".85"/>
    </g>

    <!-- central medallion -->
    <path d="M248 526 C300 470 400 440 497 420 V526 Z" fill="var(--brand-blue)"/>
    <circle cx="367" cy="263" r="152" fill="var(--black-arc)"/>
    <path d="M455 140 C475 130 495 125 520 120 L520 410 C495 405 475 395 455 385 Z" fill="var(--black-arc)"/>
    <circle cx="367" cy="263" r="137" fill="var(--brand-blue)"/>
    <circle cx="367" cy="263" r="124" fill="#ffffff"/>
    <g role="img" aria-label="Photo of a small white model house resting on paperwork">
      <circle cx="367" cy="263" r="123" fill="#dcdcdc"/>
    </g>

    <!-- about panel portraits -->
    <circle cx="52" cy="54" r="64" fill="var(--brand-blue)"/>
    <g role="img" aria-label="Portrait photo of a team member in a suit outdoors">
      <circle cx="52" cy="54" r="59" fill="#8a7a72"/>
    </g>
    <circle cx="171" cy="57" r="77" fill="#ffffff"/>
    <circle cx="171" cy="57" r="74" fill="var(--brand-blue)"/>
    <g role="img" aria-label="Portrait photo of a team member in a checked shirt">
      <circle cx="171" cy="57" r="67" fill="#4b4b4b"/>
    </g>
  </svg>

  <div class="panel panel--1">
    <div class="about">
      <h1>About Us</h1>
      <p>At Bay &amp; Meadow Property Services, we combine boots-on-the-ground experience with next-level strategy to unlock value in every square foot. Whether it’s transforming a vacant lot into a high-performing storage facility or managing a multi-unit short-stay portfolio remotely, we specialize in making real estate work smarter—for you.</p>
      <p>We are operators, builders, and investors who understand the intricacies of today’s most lucrative real estate verticals: Short-Term Rentals (STRs), Residential Rentals, and Mini/Maxi Storage Facilities. We don’t just offer services—we deliver outcomes that scale wealth, reduce risk, and free up your time.</p>
      <h2>Why Work With Us?</h2>
      <p class="reason"><b>End-to-End Execution:</b> From off-market sourcing to design, construction, management, and exit—we do it all.</p>
      <p class="reason"><b>Niche Market Focus:</b> STRs and Storage are two of the fastest-growing real estate classes. We help you dominate both.</p>
      <p class="reason"><b>Proven Track Record:</b> We’ve built and managed profitable assets from scratch—and helped others do the same.</p>
      <p class="reason"><b>System-Driven Efficiency:</b> We harness automation for pricing, bookings, leasing, and reporting so your assets work harder, not you.</p>
      <p class="reason"><b>Flexible Partnership:</b> Hands-on or hands-off, we support your style of investing.</p>
    </div>
  </div>

  <div class="panel panel--2">
    <p class="contact contact--phone">(555) 014-2290</p>
    <p class="contact contact--email">info@bayandmeadowproperty.example</p>
    <p class="contact contact--address">412 Alder Lane<br>Greenfield, WI 53000</p>
  </div>

  <div class="panel panel--3">
    <p class="brand-name">Bay &amp; Meadow</p>
    <h1 class="cover-title"><span class="dark">Grounded<br>in Expertise.</span><br><span class="light">Built for<br>Performance.</span></h1>
    <p class="cover-tagline">Let’s build something valuable—together.</p>
  </div>
</section>

<!-- Inside of the brochure -->
<section class="sheet sheet--inside" aria-label="Brochure inside">
  <svg class="sheet-art" viewBox="0 0 745 526">
    <defs>
      <linearGradient id="mistFade" x1="0" y1="0" x2="1" y2="1">
        <stop offset="0" stop-color="#cfe6f1"/><stop offset="1" stop-color="#f4f9fc"/>
      </linearGradient>
      <linearGradient id="mistFadeRight" x1="1" y1="0" x2="0" y2="1">
        <stop offset="0" stop-color="#cfe6f1"/><stop offset="1" stop-color="#ffffff"/>
      </linearGradient>
      <linearGradient id="aerialTones2" x1="0" y1="0" x2="1" y2="1">
        <stop offset="0" stop-color="#4f8a3e"/><stop offset=".6" stop-color="#6f9a5c"/><stop offset="1" stop-color="#8a8f84"/>
      </linearGradient>
      <linearGradient id="storageTones" x1="0" y1="0" x2="1" y2="1">
        <stop offset="0" stop-color="#8aa7b8"/><stop offset=".6" stop-color="#5d7f96"/><stop offset="1" stop-color="#3a4c5e"/>
      </linearGradient>
      <linearGradient id="bedroomTones" x1="0" y1="0" x2="0" y2="1">
        <stop offset="0" stop-color="#e9eef2"/><stop offset="1" stop-color="#c9d3da"/>
      </linearGradient>
      <clipPath id="panelOne"><rect x="0" y="0" width="248" height="526"/></clipPath>
      <clipPath id="panelThree"><rect x="497" y="0" width="248" height="526"/></clipPath>
    </defs>

    <!-- residential panel -->
    <g clip-path="url(#panelOne)">
      <rect x="0" y="0" width="248" height="526" fill="url(#mistFade)"/>
      <g role="img" aria-label="Aerial photo of a green residential neighbourhood">
        <path d="M0 0 H248 V200 C200 170 120 160 0 195 Z" fill="url(#aerialTones2)"/>
      </g>
    </g>

    <!-- short-term panel -->
    <rect x="248" y="0" width="249" height="526" fill="var(--brand-blue)"/>
    <circle cx="372" cy="140" r="172" fill="#e9f5fa" opacity=".55"/>
    <circle cx="372" cy="140" r="150" fill="none" stroke="#ffffff" stroke-width="2" opacity=".85"/>
    <circle cx="372" cy="140" r="138" fill="#f2f8fb" opacity=".7"/>
    <g role="img" aria-label="Photo of a bright guest bedroom with pillows and a bedside lamp">
      <circle cx="372" cy="140" r="122" fill="url(#bedroomTones)"/>
    </g>

    <!-- storage panel -->
    <g clip-path="url(#panelThree)">
      <rect x="497" y="0" width="248" height="526" fill="url(#mistFadeRight)"/>
      <g role="img" aria-label="Aerial photo of self-storage buildings with blue roofs">
        <path d="M520 0 H745 V195 C690 170 610 165 520 210 Z" fill="url(#storageTones)"/>
      </g>
      <path d="M497 0 C540 60 545 150 510 230 L497 240 Z" fill="#dbecf5"/>
    </g>
  </svg>

  <div class="panel panel--1">
    <div class="service residential">
      <h2>Residential Rental</h2>
      <p>At Bay &amp; Meadow Property Services, we specialize in helping investors uncover profitable and strategic residential real estate opportunities before they hit the mainstream market. Whether you’re building a new portfolio or expanding an existing one, our data-driven insights, local expertise, and industry connections empower you to make confident, forward-thinking investment decisions. We don’t just find properties—we find potential.</p>
      <h3>Property &amp; Rental Management<br>Built for Results</h3>
      <p class="small">Owning rental properties should build wealth—not stress. Our full-service unit and property management solutions handle everything from tenant placement to maintenance, ensuring your assets operate efficiently, legally, and profitably at every stage.</p>
      <p class="callout">Focus on Your<br>Portfolio—We’ll Handle<br>the Rest</p>
    </div>
  </div>

  <div class="panel panel--2">
    <div class="service short-term">
      <h2>Short-Term Rental</h2>
      <p>At Bay &amp; Meadow Property Services, we specialize in identifying lucrative and under-the-radar opportunities in the short-term rental sector. Whether you’re a first-time host or an institutional investor, we help you capitalize on the booming STR economy through strategic investments, regulatory compliance, and optimized operations.</p>
      <p class="callout">Spend Your Time on You,<br>We’ll Handle the Details</p>
    </div>
  </div>

  <div class="panel panel--3">
    <div class="service storage">
      <h2>Storage Facility Rental</h2>
      <p>At Bay &amp; Meadow Storage Solutions, we specialize in identifying profitable and scalable investment opportunities in the high-demand storage sector. Whether you’re entering the self-storage space or expanding an existing portfolio, we help you capitalize on the growing need for flexible, secure storage solutions across urban and suburban markets.</p>
      <p class="callout">Focus on Returns,<br>Not Logistics</p>
      <p class="closing">We manage every aspect so<br>you can focus on scaling<br>your investment portfolio.</p>
    </div>
  </div>
</section>

</body>
</html>
```